Vet Project for Web Application

We are developing a web app / forms to allow a Vet to record information when visiting a farm - eg to test animals for TB.
Needs to be clean and fresh, not cluttered.
Using standard web form design elements so that the user don't have to think.
Needs to use elements of the colours from the logo.

We will need a standard template page which we can base each of our webforms on, so we will need
standard web elements (labels, text boxes, radio buttons etc)
data grids
buttons
menus
error messages

Target Market(s)

Vets for farm animals

Number of Pages Required

1 page

Font styles to use
Sans Serif

Requirements
Must have
• Simple form elements. Intuitive. Obvious. Follow the colour pallette in the logo
Should not have
• elements that need instruction to use

```html
<!DOCTYPE html>
<html lang="en">
<head>
<meta charset="utf-8">
<title>Vet Dashboard</title>
<link href="https://fonts.googleapis.com/css2?family=Poppins:wght@400;500;600&family=Roboto:wght@400;500&display=swap" rel="stylesheet">
<style>
:root{
  --sidebar:#251a3a;
  --green:#7fc125;
  --blue:#1f7fc9;
  --ink:#1e1b2e;
  --muted:#5a5a66;
  --page:#f3f4f8;
  --line:#e2e3ea;
  --white:#fff;
}
*{box-sizing:border-box;margin:0;padding:0}
html,body{width:1200px;height:841px;overflow:hidden}
body{font-family:'Poppins',sans-serif;background:var(--page);color:var(--ink);position:relative}
.sidebar{position:absolute;left:0;top:0;width:173px;height:841px;background:var(--sidebar);border-radius:0 0 6px 0}
.brand{position:absolute;left:24px;top:24px;display:flex;align-items:center;gap:7px;color:#6fb3e8;font-weight:500;font-size:22px;letter-spacing:2px}
.brand-mark{width:12px;height:12px;background:var(--green)}
.nav{position:absolute;left:0;top:83px;width:173px;list-style:none}
.nav li{height:35.3px;display:flex;align-items:center;padding-left:24px;gap:13px;color:#fff;font-family:'Roboto',sans-serif;font-weight:500;font-size:11.3px}
.nav li svg{width:12px;height:12px;fill:#fff;flex:none}
.nav li.active{margin-left:9px;padding-left:16px;height:31px;margin-bottom:10px;background:var(--green);border-radius:16px 0 0 16px}
.topbar{position:absolute;left:173px;top:0;width:1027px;height:60px;background:var(--white)}
.page-title{position:absolute;left:27px;top:17px;font-size:19.5px;font-weight:600}
.search{position:absolute;left:587px;top:14px;width:201px;height:33px;border:1px solid var(--line);border-radius:17px;background:#f8f8fb;font-size:9.5px;color:#777;padding:10px 16px}
.search svg{position:absolute;right:12px;top:9px}
.icon-btn{position:absolute;top:17px;width:27px;height:27px;border-radius:50%;background:#f0f0f4;border:1px solid var(--line)}
.icon-btn svg{position:absolute;left:7px;top:7px}
.dot{position:absolute;right:0;top:1px;width:5px;height:5px;border-radius:50%;background:var(--green)}
.user{position:absolute;left:901px;top:15px;display:flex;align-items:center;gap:7px;font-size:11px;font-weight:500}
.avatar{width:30px;height:30px;border-radius:50%;background:linear-gradient(#cfd3da,#4a4650)}
h2.dash{position:absolute;left:200px;top:96px;font-size:18.5px;font-weight:600}
.btn{position:absolute;top:93px;height:33px;border:1.5px solid var(--blue);border-radius:3px;background:var(--white);color:var(--blue);font-size:11px;font-weight:500;display:flex;align-items:center;justify-content:center}
.btn.primary{background:var(--green);border-color:var(--green);color:#fff}
.card{position:absolute;left:200px;width:974px;border:1px solid var(--line);border-radius:3px;background:var(--page)}
.card h3{position:absolute;left:17px;font-size:16.5px;font-weight:600}
.card .link{position:absolute;right:17px;color:var(--blue);font-size:13.5px;font-weight:500}
.field{position:absolute;top:73px}
.field label{display:block;font-size:12px;font-weight:500;margin-bottom:7px}
.input{width:141px;height:36px;background:#fff;border-radius:2px;box-shadow:0 1px 4px rgba(0,0,0,.08);font-family:'Roboto',sans-serif;font-size:9.5px;color:#666;padding:12px 13px;position:relative}
.input svg{position:absolute;right:12px;top:12px}
.toggle{margin-top:2px;width:47px;height:16px;border-radius:8px;background:#e6e6ec;position:relative;font-family:'Roboto',sans-serif;font-size:9px;font-weight:500;padding:2px 0 0 21px}
.toggle::before{content:"";position:absolute;left:2px;top:2px;width:12px;height:12px;border-radius:50%;background:#fff}
.add{position:absolute;left:913px;top:88px;width:43px;height:36px;background:var(--green);border-radius:2px;color:#fff;font-size:22px;display:flex;align-items:center;justify-content:center;font-weight:500}
table{position:absolute;left:16px;top:66px;width:942px;border-collapse:collapse;background:#f3f4f8}
th{height:37px;text-align:left;font-size:12.5px;font-weight:500;border-bottom:1px solid var(--line);background:#f1f2f6}
td{height:47.3px;font-size:11.5px;color:var(--muted);border-bottom:1px solid var(--line);white-space:nowrap}
th:first-child,td:first-child{padding-left:8px}
.blue{color:var(--blue)}
.pet{display:flex;align-items:center;gap:8px}
.pet-photo{width:24px;height:24px;border-radius:50%}
.pet .species{color:var(--ink)}
.time{color:var(--ink);font-weight:600}
.pill{display:inline-block;padding:0 9px;border:1.5px solid var(--green);color:var(--green);border-radius:10px;font-size:11px;line-height:17px}
.pill.todo{border-color:var(--ink);color:var(--ink)}
.acts{display:flex;justify-content:flex-end;gap:7px;padding-right:14px}
.act{width:30px;height:30px;border-radius:2px;display:flex;align-items:center;justify-content:center;background:var(--green)}
.act.dark{background:var(--sidebar)}
.card-foot{position:absolute;left:0;bottom:0;width:972px;height:50px;background:#fff}
.showing{position:absolute;left:16px;top:6px;font-size:12.5px;font-weight:500;color:var(--muted)}
.pg{position:absolute;top:0;height:27px;border:1px solid #bfc4cf;border-radius:2px;display:flex;align-items:center;justify-content:center;font-size:12px;color:var(--blue)}
.pg.plain{border:none}
</style>
</head>
<body>
<aside class="sidebar">
  <div class="brand"><span>HERDLOG</span><span class="brand-mark"></span></div>
  <ul class="nav">
    <li class="active"><svg viewBox="0 0 12 12"><circle cx="6" cy="6" r="6"/></svg>Dashboard</li>
    <li><svg viewBox="0 0 12 12"><circle cx="4" cy="4" r="2.5"/><circle cx="9" cy="4" r="2.5"/><rect x="1" y="7" width="11" height="5" rx="2"/></svg>Teams</li>
    <li><svg viewBox="0 0 12 12"><path d="M6 0v6h6A6 6 0 1 1 6 0z"/></svg>Statistics</li>
    <li><svg viewBox="0 0 12 12"><rect x="0" y="1" width="12" height="11" rx="1"/></svg>Calendars</li>
    <li><svg viewBox="0 0 12 12"><path d="M6 0a4 4 0 0 1 4 4c0 3-4 8-4 8S2 7 2 4a4 4 0 0 1 4-4z"/></svg>Location</li>
    <li><svg viewBox="0 0 12 12"><rect x="1.5" y="0" width="9" height="12" rx="1"/></svg>Reports</li>
    <li><svg viewBox="0 0 12 12"><path d="M1 11 10 2l1 1-9 9z"/></svg>Vaccinations</li>
    <li><svg viewBox="0 0 12 12"><path d="M6 0l6 11H0z"/></svg>Evaluations</li>
    <li><svg viewBox="0 0 12 12"><rect x="0" y="0" width="8" height="10"/><rect x="4" y="3" width="8" height="9"/></svg>Compliance</li>
    <li><svg viewBox="0 0 12 12"><ellipse cx="6" cy="6" rx="6" ry="4"/></svg>View</li>
    <li><svg viewBox="0 0 12 12"><circle cx="6" cy="6" r="6"/></svg>Countries</li>
    <li><svg viewBox="0 0 12 12"><rect x="0" y="3" width="12" height="6" rx="3"/></svg>Add Booking</li>
    <li><svg viewBox="0 0 12 12"><circle cx="6" cy="6" r="6"/></svg>Questions</li>
    <li><svg viewBox="0 0 12 12"><rect x="1" y="6" width="2" height="6"/><rect x="5" y="2" width="2" height="10"/><rect x="9" y="4" width="2" height="8"/></svg>View Result</li>
    <li><svg viewBox="0 0 12 12"><circle cx="6" cy="6" r="5"/></svg>Settings</li>
    <li><svg viewBox="0 0 12 12"><rect x="2" y="5" width="8" height="7" rx="1"/><path d="M4 5V3a2 2 0 0 1 4 0v2" stroke="#fff" fill="none" stroke-width="1.5"/></svg>Logout</li>
  </ul>
</aside>

<header class="topbar">
  <h1 class="page-title">Vet to record information</h1>
  <div class="search">Search...<svg width="13" height="13" viewBox="0 0 13 13"><circle cx="5.5" cy="5.5" r="4.3" fill="none" stroke="#222" stroke-width="1.8"/><path d="M8.7 8.7 12 12" stroke="#222" stroke-width="1.8"/></svg></div>
  <div class="icon-btn" style="left:813px"><svg width="12" height="12" viewBox="0 0 12 12"><circle cx="6" cy="6" r="5" fill="none" stroke="#333" stroke-width="1"/></svg><span class="dot"></span></div>
  <div class="icon-btn" style="left:850px"><svg width="12" height="12" viewBox="0 0 12 12"><path d="M2 9h8L9 7V5a3 3 0 0 0-6 0v2z" fill="#333"/></svg></div>
  <div class="user"><div class="avatar" role="img" aria-label="User profile photo"></div>John Doe<svg width="8" height="6" viewBox="0 0 8 6"><path d="M1 1l3 3 3-3" stroke="#333" fill="none" stroke-width="1.3"/></svg></div>
</header>

<h2 class="dash">Dashboard</h2>
<div class="btn primary" style="left:777px;width:86px">New Patient</div>
<div class="btn" style="left:875px;width:80px">New Client</div>
<div class="btn" style="left:967px;width:97px">New Estimate</div>
<div class="btn" style="left:1076px;width:97px">Check In Visit</div>

<section class="card" style="top:168px;height:155px">
  <h3 style="top:22px">Quick Checkin</h3>
  <span class="link" style="top:25px">More Info</span>
  <div class="field" style="left:17px"><label>Type</label><div class="input">Day Care<svg width="8" height="11" viewBox="0 0 8 11"><path d="M4 0l4 4H0zM4 11 0 7h8z" fill="#222"/></svg></div></div>
  <div class="field" style="left:177px"><label>Date</label><div class="input">03/11/2022<svg width="11" height="11" viewBox="0 0 11 11"><rect x=".5" y="1.5" width="10" height="9" fill="none" stroke="#333"/><rect x=".5" y="1.5" width="10" height="2.5" fill="#333"/></svg></div></div>
  <div class="field" style="left:337px"><label>Duration</label><div class="input">Full Day<svg width="8" height="11" viewBox="0 0 8 11"><path d="M4 0l4 4H0zM4 11 0 7h8z" fill="#222"/></svg></div></div>
  <div class="field" style="left:497px"><label>Status</label><div class="input">Chech In<svg width="8" height="11" viewBox="0 0 8 11"><path d="M4 0l4 4H0zM4 11 0 7h8z" fill="#222"/></svg></div></div>
  <div class="field" style="left:657px"><label>Pet</label><div class="input">Pet Name</div></div>
  <div class="field" style="left:819px"><label>All Siblings</label><div class="toggle">OFF</div></div>
  <div class="add">+</div>
</section>

<section class="card" style="top:346px;height:461px">
  <h3 style="top:23px">Quick Checkin</h3>
  <span class="link" style="top:26px">Show Filters</span>
  <table>
    <thead><tr><th style="width:99px">Clients</th><th style="width:151px">Patients</th><th style="width:141px">Patient Location</th><th style="width:123px">Started</th><th style="width:117px">Reason</th><th style="width:91px">Status</th><th style="width:87px">Service</th><th style="width:40px">Pers.</th><th></th></tr></thead>
    <tbody>
      <tr><td class="blue">Jack Jordan</td><td><div class="pet"><span class="pet-photo" role="img" aria-label="Cattle photo" style="background:#5b4a38"></span><span class="blue">Jack</span><span class="species">Cattle</span></div></td><td>Farm Location-1</td><td><span class="time">15:00</span> 03/11/2022</td><td>Vaccination</td><td><span class="pill">Done</span></td><td class="blue">Surgery</td><td class="blue">RM</td><td><div class="acts"><span class="act dark"><svg width="14" height="16" viewBox="0 0 14 16"><path d="M2 1v5a4 4 0 0 0 8 0V1M6 10v2a3 3 0 0 0 6 0V9" fill="none" stroke="#fff" stroke-width="1.6"/></svg></span><span class="act"><svg width="16" height="10" viewBox="0 0 16 10"><rect x="1" y="1" width="14" height="8" fill="none" stroke="#fff" stroke-width="1.5"/><circle cx="8" cy="5" r="2" fill="#fff"/></svg></span></div></td></tr>
      <tr><td class="blue">Allison Sunday</td><td><div class="pet"><span class="pet-photo" role="img" aria-label="Sheep photo" style="background:#c9c6a4"></span><span class="blue">Hulk</span><span class="species">Sheep</span></div></td><td>Farm Location-2</td><td><span class="time">14:30</span> 03/11/2022</td><td>Wellness Visit</td><td><span class="pill todo">To Do</span></td><td class="blue">Surgery</td><td class="blue">TT</td><td><div class="acts"><span class="act"><svg width="14" height="16" viewBox="0 0 14 16"><path d="M2 1v5a4 4 0 0 0 8 0V1M6 10v2a3 3 0 0 0 6 0V9" fill="none" stroke="#fff" stroke-width="1.6"/></svg></span></div></td></tr>
      <tr><td class="blue">Marilyn Mc Bird</td><td><div class="pet"><span class="pet-photo" role="img" aria-label="Goat photo" style="background:#a99a6e"></span><span class="blue">Wilma</span><span class="species">Goat</span></div></td><td>Farm Location-3</td><td><span class="time">14:00</span> 03/11/2022</td><td>Vaccination</td><td><span class="pill">Done</span></td><td class="blue">Surgery</td><td class="blue">RM</td><td><div class="acts"><span class="act dark"><svg width="14" height="16" viewBox="0 0 14 16"><path d="M2 1v5a4 4 0 0 0 8 0V1M6 10v2a3 3 0 0 0 6 0V9" fill="none" stroke="#fff" stroke-width="1.6"/></svg></span><span class="act"><svg width="16" height="10" viewBox="0 0 16 10"><rect x="1" y="1" width="14" height="8" fill="none" stroke="#fff" stroke-width="1.5"/><circle cx="8" cy="5" r="2" fill="#fff"/></svg></span></div></td></tr>
      <tr><td class="blue">Jack Brewer</td><td><div class="pet"><span class="pet-photo" role="img" aria-label="Pig photo" style="background:#d9a9a0"></span><span class="blue">Jack</span><span class="species">Pig</span></div></td><td>Farm Location-4</td><td><span class="time">13:30</span> 03/11/2022</td><td>Wellness Visit</td><td><span class="pill todo">To Do</span></td><td class="blue">Surgery</td><td class="blue">TT</td><td><div class="acts"><span class="act"><svg width="14" height="16" viewBox="0 0 14 16"><path d="M2 1v5a4 4 0 0 0 8 0V1M6 10v2a3 3 0 0 0 6 0V9" fill="none" stroke="#fff" stroke-width="1.6"/></svg></span></div></td></tr>
      <tr><td class="blue">Ellie Johnson</td><td><div class="pet"><span class="pet-photo" role="img" aria-label="Horse photo" style="background:#5d6a52"></span><span class="blue">Joana</span><span class="species">Horse</span></div></td><td>Farm Location-5</td><td><span class="time">13:00</span> 03/11/2022</td><td>Vaccination</td><td><span class="pill">Done</span></td><td class="blue">Surgery</td><td class="blue">RM</td><td><div class="acts"><span class="act dark"><svg width="14" height="16" viewBox="0 0 14 16"><path d="M2 1v5a4 4 0 0 0 8 0V1M6 10v2a3 3 0 0 0 6 0V9" fill="none" stroke="#fff" stroke-width="1.6"/></svg></span><span class="act"><svg width="16" height="10" viewBox="0 0 16 10"><rect x="1" y="1" width="14" height="8" fill="none" stroke="#fff" stroke-width="1.5"/><circle cx="8" cy="5" r="2" fill="#fff"/></svg></span></div></td></tr>
      <tr><td class="blue">Joe Powell</td><td><div class="pet"><span class="pet-photo" role="img" aria-label="Dog photo" style="background:#d6d4cc"></span><span class="blue">Ben</span><span class="species">Dog</span></div></td><td>Farm Location-6</td><td><span class="time">12:30</span> 03/11/2022</td><td>Wellness Visit</td><td><span class="pill todo">To Do</span></td><td class="blue">Surgery</td><td class="blue">TT</td><td><div class="acts"><span class="act"><svg width="14" height="16" viewBox="0 0 14 16"><path d="M2 1v5a4 4 0 0 0 8 0V1M6 10v2a3 3 0 0 0 6 0V9" fill="none" stroke="#fff" stroke-width="1.6"/></svg></span></div></td></tr>
    </tbody>
  </table>
  <div class="card-foot">
    <span class="showing">Showing 1 to 6 of 14 entries</span>
    <span class="pg" style="left:758px;width:40px;color:#444;gap:8px">6 <svg width="8" height="6" viewBox="0 0 8 6"><path d="M1 1l3 3 3-3" stroke="#444" fill="none" stroke-width="1.3"/></svg></span>
    <span class="pg" style="left:812px;width:26px;color:#444">&lsaquo;</span>
    <span class="pg" style="left:843px;width:26px">1</span>
    <span class="pg plain" style="left:877px;width:20px">2</span>
    <span class="pg plain" style="left:905px;width:20px">3</span>
    <span class="pg" style="left:931px;width:26px;border-color:var(--blue)">&rsaquo;</span>
  </div>
</section>
</body>
</html>
```